Create a Graphic About YOURSELF and PixelHarbor

PixelHarbor would like you (designers) to create an awesome graphic to promote YOURSELF and your profile on PixelHarbor!

Your graphic should communicate your name, your services and should mention PixelHarbor.

The design should be perfect for sharing on Chatterly. Here's an example of what we'd like http://blog.pixelharbor-example.ca/article/333/pixelharbor-launches-3000-hire-me-social-design-contest

Once you submitted your design, we'd love you to share the design ('advertisement') and promote yourself and PixelHarbor to your friends and potential customers. So make your submissions great and get your friends to vote for your design by 'Liking' it on Chatterly!

Prizes:
$1500 - "PixelHarbor Community" prize awarded to the designer with the most Chatterly 'Likes'
5 x $50 for the next 5 'most liked' designs on Chatterly

$1000 - "Hire Me" prize awarded to the designer who receives the most client invites
5 x $50 for the next 5 'most invited' designers

In summary, this is a great opportunity for you to increase your exposure to PixelHarbor customers and win cash prizes. Show off your design skills and get hired by PixelHarbor customers from around the world!

Target Market(s)

Fans, friends and customers of YOU

Industry/Entity Type

Cash

Requirements
Must have
• 1) Include your PixelHarbor user name on the graphic so customers can find you in the PixelHarbor Designer Directory
2) Include the tagline "Hire Me on PixelHarbor.com!" in your graphic design.
3) Share your design's URL on our Chatterly wall at http://chatterly-example.com/pixelharbor and get your friends to 'like' your design.
Nice to have
• 1) Include a tagline that expresses your design approach/philosophy
2) Artwork dimensions: 403 x 403 px
3) You can submit more than 1 design!
Should not have
• You must own the copyright of any images you use including stock imagery.

```html
<!DOCTYPE html>
<html lang="en">
<head>
<meta charset="utf-8">
<title>Hire Me on PixelHarbor.com!</title>
<link rel="stylesheet" href="https://fonts.googleapis.com/css2?family=Questrial&family=Teko:wght@500&family=Yellowtail&display=swap">
<style>
  :root {
    --ink: #3d3d3d;
    --accent: #d4134a;
    --band: #444444;
    --paper-light: #f6f6f6;
    --paper-mid: #ececec;
    --paper-dark: #dcdcdc;
    --rule: #bdbdbd;
    --services-ink: #222222;
    --white: #ffffff;
  }
  html, body {
    margin: 0;
    padding: 0;
    width: 1200px;
    height: 1200px;
    overflow: hidden;
  }
  .poster {
    position: relative;
    width: 1200px;
    height: 1200px;
    overflow: hidden;
    background: radial-gradient(ellipse at 50% 40%, var(--paper-light) 0%, var(--paper-mid) 55%, var(--paper-dark) 100%);
    color: var(--ink);
  }
  .headline {
    position: absolute;
    top: 36px;
    left: 0;
    width: 100%;
    margin: 0;
    text-align: center;
    font-family: "Teko", "Oswald", sans-serif;
    font-weight: 500;
    font-size: 96px;
    line-height: 1;
    letter-spacing: 2px;
    color: var(--ink);
  }
  .username {
    position: absolute;
    top: 250px;
    left: 0;
    width: 1200px;
    height: 160px;
  }
  .username text {
    font-family: "Questrial", "Century Gothic", sans-serif;
    font-size: 140px;
    fill: var(--ink);
  }
  .username .marker { fill: var(--accent); }
  .divider {
    position: absolute;
    top: 438px;
    left: 24px;
    width: 1152px;
    height: 2px;
    background: var(--rule);
  }
  .services {
    position: absolute;
    top: 456px;
    left: 0;
    width: 1200px;
    height: 50px;
  }
  .services text {
    font-family: "Questrial", "Century Gothic", sans-serif;
    font-size: 32px;
    fill: var(--services-ink);
  }
  .tagline {
    position: absolute;
    margin: 0;
    font-family: "Yellowtail", cursive;
    font-size: 104px;
    line-height: 1;
    color: var(--ink);
    white-space: nowrap;
  }
  .tagline .accent { color: var(--accent); }
  .tagline-first { top: 548px; left: 60px; }
  .tagline-second { top: 680px; left: 630px; }
  .hire-band {
    position: absolute;
    top: 850px;
    left: 0;
    width: 1200px;
    height: 160px;
    background: var(--band);
  }
  .hire-band svg { display: block; }
  .hire-band text {
    font-family: "Questrial", "Century Gothic", sans-serif;
    font-size: 148px;
    fill: var(--white);
  }
  .site-url {
    position: absolute;
    top: 1058px;
    left: 0;
    width: 100%;
    margin: 0;
    text-align: center;
    font-family: "Questrial", "Century Gothic", sans-serif;
    font-size: 92px;
    line-height: 1;
    color: var(--ink);
  }
  .site-url .accent { color: var(--accent); }
</style>
</head>
<body>
  <main class="poster">
    <h2 class="headline">LOOKING FOR QUALITY DESIGNS?</h2>

    <svg class="username" viewBox="0 0 1200 160" aria-label="Tolvane Ardis">
      <circle class="marker" cx="150" cy="92" r="26"/>
      <text x="205" y="138" textLength="860" lengthAdjust="spacingAndGlyphs">Tolvane Ardis</text>
    </svg>

    <div class="divider"></div>

    <svg class="services" viewBox="0 0 1200 50" aria-label="Services">
      <text x="30" y="36" textLength="1130" lengthAdjust="spacingAndGlyphs">web design | logo design | graphic design | business card | brochures</text>
    </svg>

    <p class="tagline tagline-first"><span class="accent">Your</span> Satisfaction</p>
    <p class="tagline tagline-second"><span class="accent">My</span> Passion</p>

    <div class="hire-band">
      <svg viewBox="0 0 1200 160" width="1200" height="160" aria-label="Hire me on">
        <text x="70" y="132" textLength="1060" lengthAdjust="spacingAndGlyphs">HIRE ME ON</text>
      </svg>
    </div>

    <p class="site-url">www.<span class="accent">pixelharbor</span>.com</p>
  </main>
</body>
</html>
```